Corporate Web Redesign Project - coded

We would like redesign/refresh of our current site that would allow us to increase the depth of content and create a high quality impression for visitors.

Current site - http://corvanisystems.com/

A previous web redesign project has improved our site but it has not really reached the level we require.

Our customers are global, blue chip, organisations and a professional, corporate style of site is required.

Please note we would prefer a coded website to a just a design. We are happy to provide a zip of our current site if required.
Updates

                                   

Target Market(s)

Global oil and gas producers, KR, Tamberline, Orvadex etc.

Industry/Entity Type

It Professional

Requirements
Must have
• Design should support the level of content we currently have in the existing sitemap - although it should be expandable a site design for a large / complex site would not be appropriate

All current content / pages to be reflected in design

Must be visually appealing

Intuitive and clear navigation that is expandable

Display a high level of professionalism

Use a consistent palette of colours that complements our logo

Clean and organized layout

A way to capture visitor’s information or Call to action (i.e. contact link or form) on every page

Prominent Contact Information
Should not have
• Flash

```html
<!DOCTYPE html>
<html lang="en">
<head>
<meta charset="utf-8">
<title>Corvani Systems</title>
<link href="https://fonts.googleapis.com/css2?family=Signika:wght@400;600&family=PT+Sans+Narrow:wght@400;700&family=PT+Sans:wght@400;700&family=Arimo&display=swap" rel="stylesheet">
<style>
:root{
  --teal:#1d4a4f;
  --teal-mid:#3f6a67;
  --ink:#1a1a1a;
  --body:#222;
  --panel:#fff;
  --band-dark:#5a5a5a;
  --band-light:#c9c9c9;
  --band-pale:#ebebeb;
  --footer:#1b1b1b;
  --footer-strip:#000;
  --footer-text:#e6e6e6;
  --nav-green:#4a6a55;
}
*{margin:0;padding:0;box-sizing:border-box}
html,body{width:1120px;height:1200px;overflow:hidden;background:var(--footer)}
.page{position:relative;width:1120px;height:1200px;font-family:"Arimo",Arial,sans-serif;color:var(--body)}
.abs{position:absolute}
.band-top{left:0;top:0;width:1120px;height:137px;background:linear-gradient(#3e3e3e,#6a6a6a)}
.band-hero{left:0;top:137px;width:1120px;height:329px;background:var(--band-light)}
.band-content{left:0;top:466px;width:1120px;height:493px;background:var(--band-pale)}
.panel{left:130px;top:0;width:858px;height:959px;background:var(--panel)}
.header-shadow{left:130px;top:131px;width:858px;height:6px;background:linear-gradient(rgba(0,0,0,0),rgba(0,0,0,.08))}
.brand{left:153px;top:22px;display:flex;align-items:center;gap:10px;font-family:"Signika",sans-serif;font-weight:600;font-size:22px;color:var(--teal);letter-spacing:.5px}
.brand .dot{width:44px;height:44px;border-radius:50%;background:var(--teal-mid)}
.phone{left:781px;top:38px;display:flex;align-items:center;gap:8px;font-family:"Signika",sans-serif;font-size:19px;color:#444}
.nav{left:510px;top:91px;display:flex;align-items:center;font-family:"Signika",sans-serif;font-size:13px;color:#222}
.nav a{color:inherit;text-decoration:none}
.nav .home{background:var(--nav-green);color:#fff;width:63px;height:24px;border-radius:3px;display:flex;align-items:center;justify-content:center}
.hero-title{left:144px;top:158px;font-family:"Signika",sans-serif;font-weight:600;font-size:40px;line-height:42px;color:var(--teal)}
.hero-text{left:146px;top:254px;width:296px;font-size:11.2px;line-height:17.2px;color:#111}
.btn-more{left:145px;top:388px;width:152px;height:43px;border-radius:22px;background:linear-gradient(#6f8c8c,#355857);box-shadow:0 3px 4px rgba(0,0,0,.25);display:flex;align-items:center;justify-content:space-between;padding:0 10px 0 18px;font-family:"Arimo",sans-serif;font-weight:700;font-size:15px;color:#fff}
.btn-more .arr{width:26px;height:26px;border-radius:50%;background:#f3f3f3;display:flex;align-items:center;justify-content:center}
.dots{left:152px;top:450px;display:flex;gap:7px}
.dots span{width:16px;height:16px;border-radius:50%;background:radial-gradient(#fff,#bdbdbd)}
.dots .on{background:radial-gradient(#6f9577,#2f4b36)}
.hero-frame{left:458px;top:142px;width:527px;height:328px;border:1px solid #e1e1e1;background:#fff}
.hero-photo{left:463px;top:147px;width:518px;height:318px;background:linear-gradient(120deg,#b9cce0 0%,#8f8a7a 40%,#5f646b 70%,#c9d3dd 100%)}
.divider-shadow{left:100px;top:470px;width:920px;height:12px;background:radial-gradient(ellipse at top,rgba(0,0,0,.08),rgba(0,0,0,0) 70%)}
.section-title{left:143px;top:500px;font-family:"PT Sans Narrow",sans-serif;font-size:23px;color:var(--ink)}
.fold{left:132px;top:540px;width:206px;height:166px;background:linear-gradient(135deg,#e4e4e4,#fff 50%,#e4e4e4)}
.intro-photo{left:149px;top:559px;width:174px;height:124px;background:linear-gradient(135deg,#d9dde2,#aeb9c6 55%,#7a8796)}
.intro-text{left:351px;top:555px;width:632px;font-size:11.2px;line-height:15.5px;color:#1a1a1a}
.intro-text p+p{margin-top:15.5px}
.feature{top:724px;width:200px}
.feature h3{font-family:"Signika",sans-serif;font-weight:400;font-size:15.5px;color:var(--teal);margin-bottom:10px}
.feature .body{font-size:10.8px;line-height:14.6px;color:#222;padding-left:4px}
.feature .ico{float:left;width:22px;height:22px;margin:2px 6px 0 0}
.feature .more{display:flex;justify-content:flex-end;align-items:center;gap:6px;margin-top:8px;font-size:11px;color:#222;padding-right:6px}
.feature .more i{width:16px;height:16px;border-radius:50%;background:#8a8a8a;display:flex;align-items:center;justify-content:center}
.vline{top:728px;width:1px;height:106px;background:#d6d6d6}
.partners{left:143px;top:886px;width:830px;height:67px;border-radius:22px;background:linear-gradient(#fdfdfd,#e2e2e2);border:1px solid #d2d2d2;display:flex;align-items:center;justify-content:space-between;padding:0 10px}
.partners ul{list-style:none;display:flex;flex:1;justify-content:space-around;align-items:center;font-family:"Signika",sans-serif;font-weight:600;font-size:15px;color:#4b4b4b}
.f-col{top:983px}
.f-col h4{font-family:"Signika",sans-serif;font-weight:400;font-size:17.5px;color:#fff;margin-bottom:10px}
.f-col ul{list-style:none;font-family:"PT Sans",sans-serif;font-size:11px;line-height:19px;color:var(--footer-text);padding-left:3px}
.f-line{width:1px;background:#444}
.social{left:818px;top:986px;display:flex;gap:5px}
.social span{width:33px;height:32px;background:#4a4a4a;color:#fff;font-family:"PT Sans",sans-serif;font-size:10px;display:flex;align-items:center;justify-content:center}
.social span+span+span+span{margin-left:8px}
.f-rule{left:797px;top:1042px;width:175px;height:1px;background:#444}
.f-brand{left:801px;top:1070px;display:flex;align-items:center;gap:8px;font-family:"Signika",sans-serif;font-weight:600;font-size:17px;color:#bdbdbd}
.f-brand .dot{width:36px;height:36px;border-radius:50%;background:#8b8b8b}
.strip{left:0;top:1133px;width:1120px;height:37px;background:var(--footer-strip)}
.legal{left:134px;font-family:"PT Sans",sans-serif;font-size:10px;color:#cfcfcf}
.legal b{font-weight:400;margin:0 5px;color:#777}
</style>
</head>
<body>
<div class="page">
  <div class="abs band-top"></div>
  <div class="abs band-hero"></div>
  <div class="abs band-content"></div>
  <div class="abs panel"></div>
  <div class="abs header-shadow"></div>

  <header>
    <div class="abs brand"><span class="dot"></span>CORVANI SYSTEMS</div>
    <div class="abs phone">
      <svg width="28" height="26" viewBox="0 0 28 26" aria-hidden="true"><path d="M2 9c0-5 24-5 24 0v2h-6V8H8v3H2z" fill="#111"/><path d="M6 12h16l3 12H3z" fill="#111"/><circle cx="14" cy="17" r="4" fill="#fff"/><circle cx="14" cy="17" r="2" fill="#111"/></svg>
      44(0)1632 960418
    </div>
    <nav class="abs nav">
      <a class="home">Home</a>
      <a style="margin-left:40px">News</a>
      <a style="margin-left:56px">About Us</a>
      <a style="margin-left:56px">Solutions</a>
      <a style="margin-left:55px">Contact Us</a>
    </nav>
  </header>

  <section class="hero">
    <h1 class="abs hero-title">Corvani<br>Systems</h1>
    <p class="abs hero-text">We are an integrated software and consulting organization, helping companies across the globe to better manage the Business of Drilling Wells, improving capital globe to better manage the Business of Drillingglobe to better manage the Business of Drillingglobe to better manage the Business of Drillingglobe to better manage.</p>
    <div class="abs btn-more">Read More<span class="arr"><svg width="10" height="10" viewBox="0 0 10 10"><path d="M3 1l5 4-5 4z" fill="#355857"/></svg></span></div>
    <div class="abs dots"><span></span><span class="on"></span><span></span><span></span></div>
    <div class="abs hero-frame"></div>
    <div class="abs hero-photo" role="img" aria-label="Photo of two business people holding documents in front of an offshore drilling rig"></div>
  </section>

  <div class="abs divider-shadow"></div>

  <section>
    <h2 class="abs section-title">Better manage the business of drilling wells.</h2>
    <div class="abs fold"></div>
    <div class="abs intro-photo" role="img" aria-label="Photo of a man working on a laptop"></div>
    <div class="abs intro-text">
      <p>We are an&nbsp; and consulting organization, helping companies across the globe to better manage the Business of Drilling Wells, improving capital allocation and&nbsp; and consulting organization, helping companies across the globe to better manage the Business of Drilling Wells, improving capital allocation and&nbsp; and consulting organization, helping companies across the globe to better manage the Business of Drilling Wells, improving capital allocation and&nbsp; and consulting organization, helping companies across the globe to better manage the Business of Drilling Wells,</p>
      <p>Improving capital allocation and integrated software and consulting organization, helping companies across the globe to better manage the Business of Drilling Wells, improving capital allocation and saving money.</p>
    </div>

    <div class="abs feature" style="left:150px">
      <h3>Time &amp; Cost Estimation</h3>
      <div class="body"><svg class="ico" viewBox="0 0 22 22"><circle cx="11" cy="11" r="10" fill="#111"/><path d="M11 5v6l4 3" stroke="#fff" stroke-width="2" fill="none"/></svg>Latin literature from 45 BC, making it over&nbsp; Ashford-old. College in Virginia2000 years&nbsp; old. Martin Hale Latin in Virginia 2000 yearsprofessor.</div>
      <div class="more">Read more <i><svg width="8" height="8" viewBox="0 0 8 8"><path d="M2 1l4 3-4 3" stroke="#fff" stroke-width="1.5" fill="none"/></svg></i></div>
    </div>
    <div class="abs vline" style="left:345px"></div>
    <div class="abs feature" style="left:366px">
      <h3>Materials &amp; Cost Control</h3>
      <div class="body"><svg class="ico" viewBox="0 0 22 22"><circle cx="11" cy="11" r="8" fill="#222" stroke="#222" stroke-width="4" stroke-dasharray="3 2.3"/><circle cx="11" cy="11" r="3" fill="#fff"/></svg>Latin literature from 45 BC, making it over&nbsp; Ashford-old. College in Virginia2000 years&nbsp; old. Martin Hale Latin in Virginia 2000 yearsprofessor.</div>
      <div class="more">Read more <i><svg width="8" height="8" viewBox="0 0 8 8"><path d="M2 1l4 3-4 3" stroke="#fff" stroke-width="1.5" fill="none"/></svg></i></div>
    </div>
    <div class="abs vline" style="left:562px"></div>
    <div class="abs feature" style="left:590px">
      <h3>Lessons Learned</h3>
      <div class="body"><svg class="ico" viewBox="0 0 22 22"><rect x="1" y="3" width="20" height="14" rx="2" fill="#222"/><rect x="3" y="5" width="16" height="8" fill="#666"/><rect x="0" y="17" width="22" height="3" fill="#444"/></svg>Latin literature from 45 BC, making it over&nbsp; Ashford-old. College in Virginia2000 years&nbsp; old. Martin Hale Latin in Virginia 2000 yearsprofessor.</div>
      <div class="more">Read more <i><svg width="8" height="8" viewBox="0 0 8 8"><path d="M2 1l4 3-4 3" stroke="#fff" stroke-width="1.5" fill="none"/></svg></i></div>
    </div>
    <div class="abs vline" style="left:780px"></div>
    <div class="abs feature" style="left:804px">
      <h3>Services &amp; Consulting</h3>
      <div class="body"><svg class="ico" viewBox="0 0 22 22"><circle cx="8" cy="14" r="5" fill="#222" stroke="#222" stroke-width="3" stroke-dasharray="2 1.8"/><circle cx="8" cy="14" r="2" fill="#fff"/><circle cx="16" cy="6" r="3.5" fill="#444" stroke="#444" stroke-width="2" stroke-dasharray="1.6 1.4"/></svg>Latin literature from 45 BC, making it over&nbsp; Ashford-old. College in Virginia2000 years&nbsp; old. Martin Hale Latin in Virginia 2000 yearsprofessor.</div>
      <div class="more">Read more <i><svg width="8" height="8" viewBox="0 0 8 8"><path d="M2 1l4 3-4 3" stroke="#fff" stroke-width="1.5" fill="none"/></svg></i></div>
    </div>

    <div class="abs partners">
      <svg width="16" height="26" viewBox="0 0 16 26"><path d="M12 2L3 13l9 11" stroke="#222" stroke-width="3" fill="none"/></svg>
      <ul>
        <li>Halvern</li><li>Orvadex</li><li>Torsa</li><li>Nordvik</li><li>Caldera</li><li>Brightholm</li><li>Meridane</li><li>Arrowpeak</li><li>KR</li>
      </ul>
      <svg width="16" height="26" viewBox="0 0 16 26"><path d="M4 2l9 11-9 11" stroke="#222" stroke-width="3" fill="none"/></svg>
    </div>
  </section>

  <footer>
    <div class="abs f-col" style="left:165px"><h4>Quick Links</h4>
      <ul><li>Lorem ipsum dolor sit</li><li>Amet consectetuer</li><li>Adipiscing elit</li><li>Praesent vestibulum</li><li>Molestie lacus aenean</li></ul></div>
    <div class="abs f-line" style="left:339px;top:1003px;height:113px"></div>
    <div class="abs f-col" style="left:392px"><h4>How it Works</h4>
      <ul><li>Lorem ipsum dolor sit</li><li>Amet consectetuer</li><li>Adipiscing elit</li><li>Praesent vestibulum</li><li>Molestie lacus aenean</li></ul></div>
    <div class="abs f-line" style="left:558px;top:1010px;height:112px"></div>
    <div class="abs f-col" style="left:591px;top:985px"><h4>Contact Us</h4>
      <ul><li>12 Harrow Quay</li><li>Dunmore, DN4 2QT</li><li>Phone:+44(0)1632 960418</li><li>Email:info@corvanisystems.com</li></ul></div>
    <div class="abs social"><span>Feed</span><span>Share</span><span>Post</span><span>Chat</span></div>
    <div class="abs f-rule"></div>
    <div class="abs f-brand"><span class="dot"></span>CORVANI SYSTEMS</div>
    <div class="abs strip"></div>
    <div class="abs legal" style="top:1137px">Home<b>|</b>News<b>|</b>About Us<b>|</b>Solutions<b>|</b>Contact Us</div>
    <div class="abs legal" style="top:1154px">© 2013 Corvani Systems.<b></b>FAQ<b>|</b>Privacy Policy<b>|</b>Site Map.</div>
  </footer>
</div>
</body>
</html>
```